Commercial Construction Company

We need a business card design based on our current logo. We are a commercial general contractor based in Southern California that specializes in bank remodels. We would like to see designs that incorporate dark blue. The final design should portray an image of professionalism and quality.

If possible, I would like to add metallic foil to the design. Thank you

```html
<!DOCTYPE html>
<html lang="en">
<head>
<meta charset="utf-8">
<title>Kestrel Commercial Builders – Business Card</title>
<link rel="stylesheet" href="https://fonts.googleapis.com/css2?family=Montserrat:wght@400;500;600;800&display=swap">
<style>
  :root {
    --page: #ffffff;
    --navy-deep: #111a4a;
    --navy: #1c2a6e;
    --blue: #1f5fc4;
    --blue-bright: #3a8bff;
    --ink: #15171c;
    --white: #ffffff;
    --muted: #c9d3f2;
    --faint: rgba(160, 176, 230, 0.22);
  }
  * { margin: 0; padding: 0; box-sizing: border-box; }
  html, body {
    width: 1200px; height: 1200px; overflow: hidden;
    background: var(--page);
    font-family: "Montserrat", sans-serif;
  }
  .sheet {
    width: 1200px; height: 1200px;
    display: flex; align-items: center; justify-content: center; gap: 60px;
  }
  .card { width: 520px; height: 312px; display: block; box-shadow: 0 6px 18px rgba(0,0,0,0.18); }
  .brand-name { font-family: "Montserrat", sans-serif; font-weight: 800; fill: var(--ink); }
  .brand-dot { fill: var(--blue); }
  .founder-name { font-weight: 500; fill: var(--white); }
  .founder-role { font-weight: 400; fill: var(--muted); }
  .contact-line { font-weight: 600; fill: var(--white); }
  .contact-icon { fill: var(--white); }
  .watermark-name { font-weight: 800; fill: var(--faint); }
</style>
</head>
<body>
<main class="sheet">

  <!-- Card front -->
  <svg class="card card-front" viewBox="0 0 543 326" xmlns="http://www.w3.org/2000/svg" aria-label="Business card front">
    <defs>
      <linearGradient id="bandLeft" x1="0" y1="0" x2="1" y2="1">
        <stop offset="0" stop-color="#2a63c9"/>
        <stop offset="0.45" stop-color="#16296b"/>
        <stop offset="1" stop-color="#0c1440"/>
      </linearGradient>
      <linearGradient id="bandRight" x1="1" y1="0" x2="0" y2="1">
        <stop offset="0" stop-color="#0c1440"/>
        <stop offset="0.6" stop-color="#17307a"/>
        <stop offset="1" stop-color="#3a8bff"/>
      </linearGradient>
      <linearGradient id="shadeLeft" x1="0" y1="0" x2="1" y2="0">
        <stop offset="0" stop-color="#9aa3b5" stop-opacity="0.6"/>
        <stop offset="1" stop-color="#ffffff" stop-opacity="0"/>
      </linearGradient>
    </defs>
    <rect width="543" height="326" fill="#ffffff"/>
    <!-- soft grey fold shading -->
    <polygon points="0,30 0,326 245,326" fill="url(#shadeLeft)"/>
    <polygon points="390,0 543,0 543,265" fill="#b7bdc9" opacity="0.45"/>
    <!-- left band -->
    <polygon points="0,48 0,326 212,326" fill="url(#bandLeft)"/>
    <polygon points="0,48 0,60 200,326 212,326" fill="var(--blue-bright)" opacity="0.75"/>
    <polygon points="0,150 0,326 120,326" fill="#0b1236" opacity="0.55"/>
    <!-- right band -->
    <polygon points="404,0 543,0 543,250" fill="url(#bandRight)"/>
    <polygon points="404,0 416,0 543,232 543,250" fill="var(--blue-bright)" opacity="0.75"/>
    <polygon points="470,0 543,0 543,120" fill="#0a1134" opacity="0.55"/>
    <!-- brand -->
    <circle class="brand-dot" cx="229" cy="170" r="12"/>
    <text class="brand-name" x="250" y="180" font-size="28">KESTREL</text>
  </svg>

  <!-- Card back -->
  <svg class="card card-back" viewBox="0 0 543 326" xmlns="http://www.w3.org/2000/svg" aria-label="Business card back">
    <defs>
      <radialGradient id="topGlow" cx="0.5" cy="0" r="0.45">
        <stop offset="0" stop-color="#2f7ee6"/>
        <stop offset="1" stop-color="#1c2a6e" stop-opacity="0"/>
      </radialGradient>
      <radialGradient id="bottomGlow" cx="0.5" cy="1" r="0.4">
        <stop offset="0" stop-color="#2a6fd6"/>
        <stop offset="1" stop-color="#1c2a6e" stop-opacity="0"/>
      </radialGradient>
      <linearGradient id="sketchTone" x1="0" y1="0" x2="1" y2="1">
        <stop offset="0" stop-color="#2a4aa0" stop-opacity="0.35"/>
        <stop offset="1" stop-color="#1c2a6e" stop-opacity="0"/>
      </linearGradient>
    </defs>
    <rect width="543" height="326" fill="var(--navy)"/>
    <rect width="543" height="326" fill="url(#topGlow)"/>
    <rect width="543" height="326" fill="url(#bottomGlow)"/>
    <rect x="150" y="10" width="250" height="300" fill="url(#sketchTone)" role="img" aria-label="Faint architectural building sketch"/>
    <!-- rule lines -->
    <rect x="0" y="37" width="543" height="1.6" fill="var(--blue-bright)"/>
    <rect x="0" y="288" width="543" height="1.6" fill="var(--blue-bright)"/>
    <!-- faint brand watermark -->
    <circle cx="110" cy="163" r="76" fill="none" stroke="rgba(160,176,230,0.18)" stroke-width="12"/>
    <text class="watermark-name" x="62" y="178" font-size="40">KESTREL</text>

    <!-- founder block -->
    <text class="founder-name" x="285" y="105" font-size="19">FOUNDER NAME</text>
    <text class="founder-role" x="285" y="118" font-size="8.5">CO-FOUNDER BUSINESS NAME</text>

    <g class="contact-list" font-size="8.6">
      <!-- pin -->
      <path class="contact-icon" d="M288 142 a4 4 0 0 1 8 0 c0 3 -4 7 -4 7 s-4 -4 -4 -7z M292 140.5 a1.4 1.4 0 1 0 0.01 0z" fill-rule="evenodd"/>
      <text class="contact-line" x="300" y="150">123 Dummy Road, Lorem Ipsum, Country</text>
      <!-- phone -->
      <path class="contact-icon" d="M288.5 163 c0.5-1 1.5-1.5 2-1 l1.5 2 c0.3 0.5 0 1 -0.5 1.3 c0.5 1.2 1.4 2.1 2.6 2.6 c0.3-0.5 0.8-0.8 1.3-0.5 l2 1.5 c0.5 0.5 0 1.5 -1 2 c-4 0.5 -8.5-4 -7.9-7.9z"/>
      <text class="contact-line" x="300" y="170">+00 1234 56789 9101</text>
      <!-- mail -->
      <rect class="contact-icon" x="288" y="184" width="8" height="5.5"/>
      <path d="M288 184 l4 3 l4 -3" fill="none" stroke="var(--navy)" stroke-width="0.8"/>
      <text class="contact-line" x="300" y="190">contact@websitename.com</text>
      <!-- globe -->
      <circle cx="292" cy="206" r="4" fill="none" stroke="var(--white)" stroke-width="1.1"/>
      <ellipse cx="292" cy="206" rx="1.6" ry="4" fill="none" stroke="var(--white)" stroke-width="0.8"/>
      <line x1="288" y1="206" x2="296" y2="206" stroke="var(--white)" stroke-width="0.8"/>
      <text class="contact-line" x="300" y="210">www.websitename.com</text>
    </g>
  </svg>

</main>
</body>
</html>
```